Number of Pages Required

1 page

Requirements
Must have
• An Overview / Background of the Business & Services(not for profit rescue animal farm)
• The Target Market / Audience you are trying to reach (animal lovers)
• Design Specifics; any preferences or ideas for Style, Colour, Imagery, etc (no preferences)

```html
<!DOCTYPE html>
<html lang="en">
<head>
<meta charset="utf-8">
<title>Cedar Hollow Farm</title>
<link href="https://fonts.googleapis.com/css2?family=Poppins:wght@500;600;700;800&family=Open+Sans:wght@400;600&display=swap" rel="stylesheet">
<style>
:root{
  --navy:#2d3557;
  --accent:#e8401c;
  --text:#4a4a4a;
  --light:#f4f2f2;
  --white:#ffffff;
  --rule:#b9b9b9;
}
*{box-sizing:border-box;margin:0;padding:0}
html,body{width:1200px;height:3814px;overflow:hidden}
body{font-family:"Open Sans",Arial,sans-serif;color:var(--text);background:var(--white);position:relative}
h1,h2,h3,.brand,.btn,.nav a{font-family:"Poppins",Arial,sans-serif}
.btn{display:inline-block;background:var(--accent);color:var(--white);font-weight:600;font-size:13px;letter-spacing:.3px;text-transform:uppercase;text-decoration:none;text-align:center;line-height:30px;height:30px;padding:0 22px}
.rule{width:34px;height:3px;background:var(--rule);display:block}
section,header,footer{position:absolute;left:0;width:1200px}

/* header */
.site-header{top:0;height:86px;background:var(--white);border-bottom:3px solid var(--accent);z-index:3}
.brand{position:absolute;left:142px;top:22px;font-size:30px;font-weight:700;color:var(--navy)}
.nav{position:absolute;left:497px;top:33px;display:flex;gap:14px;align-items:center}
.nav a{font-size:13px;font-weight:600;color:var(--navy);text-decoration:none;text-transform:uppercase}
.nav a.active{color:var(--accent)}
.nav .sep{color:#999;font-size:13px}

/* hero */
.hero{top:86px;height:610px;background:linear-gradient(180deg,#7fa342 0%,#8fb544 30%,#6f9a2f 65%,#5d8a26 100%)}
.hero-photo{position:absolute;inset:0}
.donate-tab{position:absolute;top:0;left:986px;width:117px;height:54px;background:var(--accent);color:var(--white);font-family:"Poppins",Arial,sans-serif;font-weight:700;font-size:15px;text-align:center;line-height:48px;clip-path:polygon(0 0,100% 0,100% 100%,50% 88%,0 100%)}
.hero-copy{position:absolute;left:748px;top:366px;color:var(--white)}
.hero-copy .kicker{font-family:"Poppins",Arial,sans-serif;font-weight:700;font-size:28px;line-height:1}
.hero-copy h1{font-size:42px;font-weight:800;line-height:1.1;margin:6px 0 18px}
.hero-copy .btn{height:44px;line-height:44px;font-size:16px;padding:0 30px}
.dots{position:absolute;left:543px;top:508px;display:flex;gap:12px}
.dots span{width:9px;height:9px;border-radius:50%;background:var(--white)}
.dots span.on{background:var(--accent);box-shadow:0 0 0 2px var(--white)}
.edge{position:absolute;left:0;width:1200px;display:block}

/* features */
.features{top:686px;height:529px;background:var(--light);text-align:center}
.section-title{font-size:34px;font-weight:700;color:var(--navy)}
.features .section-title{margin-top:43px}
.features .rule{margin:12px auto 0}
.feature-grid{display:flex;justify-content:space-between;width:970px;margin:60px auto 0}
.feature{width:215px;display:flex;flex-direction:column;align-items:center}
.feature svg{width:80px;height:80px}
.feature h3{font-size:16px;font-weight:700;color:#222;text-transform:uppercase;margin-top:36px}
.feature p{font-size:13px;line-height:18px;margin:12px 0 24px;min-height:78px}
.feature .btn{font-size:12px;height:30px;line-height:30px;padding:0 18px}

/* welcome */
.welcome{top:1215px;height:565px;background:var(--white)}
.welcome-photo{position:absolute;left:145px;top:64px;width:430px;height:439px;background:linear-gradient(180deg,#3f6e2a 0%,#5a8f2f 45%,#6fa831 70%,#4d8a22 100%)}
.welcome-copy{position:absolute;left:623px;top:100px;width:440px}
.welcome-copy .lead{font-family:"Poppins",Arial,sans-serif;font-size:30px;font-weight:500;color:var(--navy);line-height:1.1}
.welcome-copy h2{font-size:36px;font-weight:700;color:var(--navy);line-height:1.25}
.welcome-copy .rule{margin:10px 0 28px}
.welcome-copy p{font-size:15px;line-height:22px;color:#555}
.welcome-copy .btn{margin-top:30px}

/* services */
.services{top:1770px;height:640px;color:var(--white)}
.services-photo{position:absolute;inset:0;background:linear-gradient(180deg,#1e3f9a 0%,#2a56b8 40%,#4a78c8 66%,#5d8a3a 76%,#4a7a24 100%)}
.services-copy{position:absolute;left:143px;top:106px;width:380px}
.services-copy .bar{width:58px;height:4px;background:var(--white);display:block}
.services-copy h2{font-size:38px;font-weight:700;margin-top:14px;line-height:1.1}
.services-copy .intro{font-size:16px;line-height:22px;margin-top:14px}
.services-copy ul{list-style:none;margin-top:18px}
.services-copy li{font-size:15px;line-height:29px;padding-left:22px;position:relative}
.services-copy li::before{content:"›";position:absolute;left:2px;top:0;font-weight:700}
.services-copy .btn{margin-top:18px;height:28px;line-height:28px;font-size:12px;padding:0 18px}

/* get involved */
.involved{top:2402px;height:648px;background:var(--light);text-align:center}
.involved .section-title{margin-top:20px}
.involved .rule{margin:10px auto 0}
.cards{position:absolute;left:137px;top:127px;display:flex;gap:24px}
.card{width:293px;height:445px;background:var(--white);text-align:left;box-shadow:0 1px 3px rgba(0,0,0,.08)}
.card-photo{height:254px}
.card-photo.cow{background:linear-gradient(180deg,#3f6a2a,#6b4630 55%,#4e6e2d)}
.card-photo.goat{background:linear-gradient(180deg,#2f5f22,#e8ece6 55%,#4c7f2a)}
.card-photo.horses{background:linear-gradient(180deg,#7b8aa0,#8a4b2d 55%,#a8763c)}
.card-body{padding:24px 28px 0}
.card h3{font-size:19px;font-weight:700;color:#222}
.card p{font-size:13px;line-height:17px;margin-top:10px}
.card .btn{margin-top:20px;height:28px;line-height:28px;font-size:12px;padding:0 18px}
.arrow{position:absolute;top:355px;width:20px;height:30px}
.arrow.prev{left:72px}
.arrow.next{left:1102px}

/* donation */
.donation{top:3050px;height:344px;background:var(--white);text-align:center}
.donation .section-title{margin-top:72px}
.donation p{font-size:18px;line-height:28px;color:#444;width:520px;margin:18px auto 0}
.donation .btn{margin-top:34px;height:40px;line-height:40px;font-size:15px;padding:0 26px}

/* footer */
.site-footer{top:3394px;height:420px;background:var(--navy);color:var(--white)}
.footer-brand{position:absolute;left:140px;top:158px;font-family:"Poppins",Arial,sans-serif;font-size:31px;font-weight:700}
.footer-col{position:absolute;top:106px}
.footer-col h4{font-family:"Poppins",Arial,sans-serif;font-size:12px;font-weight:700;text-transform:uppercase;margin-bottom:18px}
.footer-col.contact{left:488px}
.footer-col.menu{left:770px}
.footer-col.connect{left:930px}
.contact-item{display:flex;gap:14px;font-size:11px;line-height:16px;margin-bottom:22px}
.contact-item svg{width:12px;height:12px;flex:none;margin-top:2px}
.menu ul{list-style:none}
.menu li{font-size:11px;line-height:17px}
.social{display:flex;align-items:center;gap:12px;font-size:11px;margin-bottom:16px}
.social span.dot{width:26px;height:26px;border-radius:50%;flex:none}
.dot.a{background:#3b5a9a}.dot.b{background:#1da1f2}.dot.c{background:#0d1b3d}
.copyright{position:absolute;left:0;width:1200px;top:364px;text-align:center;font-size:11px}
</style>
</head>
<body>

<header class="site-header">
  <div class="brand">Cedar Hollow Farm</div>
  <nav class="nav">
    <a href="#" class="active">Home</a><span class="sep">\</span>
    <a href="#">About Us</a><span class="sep">\</span>
    <a href="#">Meet the Animals</a><span class="sep">\</span>
    <a href="#">Get Involved</a><span class="sep">\</span>
    <a href="#">Contact Us</a>
  </nav>
</header>

<section class="hero">
  <div class="hero-photo" role="img" aria-label="Two young lambs standing on a sunny green pasture"></div>
  <div class="donate-tab">DONATE</div>
  <div class="hero-copy">
    <div class="kicker">MEET THE</div>
    <h1>CEDAR HOLLOW FARM</h1>
    <a href="#" class="btn">Read More</a>
  </div>
  <div class="dots"><span></span><span></span><span class="on"></span><span></span><span></span></div>
  <svg class="edge" style="bottom:-1px;height:46px" viewBox="0 0 1200 46" preserveAspectRatio="none">
    <path fill="#f4f2f2" d="M0 30 L40 24 L70 32 L110 20 L150 28 L190 18 L230 26 L280 14 L320 24 L360 16 L410 26 L450 12 L500 22 L540 18 L590 28 L630 16 L680 24 L720 14 L770 22 L810 10 L860 20 L900 12 L950 22 L990 8 L1040 18 L1080 6 L1120 16 L1160 4 L1200 12 L1200 46 L0 46 Z"/>
  </svg>
</section>

<section class="features">
  <h2 class="section-title">Features</h2>
  <span class="rule"></span>
  <div class="feature-grid">
    <div class="feature">
      <svg viewBox="0 0 80 80" fill="none" stroke="#2d3557" stroke-width="5" stroke-linecap="round" stroke-linejoin="round">
        <circle cx="46" cy="18" r="13" fill="#2d3557" stroke="none"/>
        <path d="M46 11v14M42 14h6a3 3 0 010 6h-4a3 3 0 000 6h6" stroke="#fff" stroke-width="2.5"/>
        <path d="M6 56l12-10h16l10 6H32M18 70l10-6h20l22-18"/>
      </svg>
      <h3>Give Monthly</h3>
      <p>Sed ut perspiciatis unde omnis iste natus error sit voluptatem accusantium doloremque laud antium, totam rem aperia m eaque ipsa quae.</p>
      <a href="#" class="btn">Become a Member</a>
    </div>
    <div class="feature">
      <svg viewBox="0 0 80 80">
        <rect x="14" y="40" width="52" height="34" fill="#2d3557"/>
        <rect x="10" y="40" width="60" height="6" fill="#2d3557"/>
        <path d="M24 32 L44 10 L58 24 L38 44 Z" fill="none" stroke="#2d3557" stroke-width="5" stroke-linejoin="round"/>
        <circle cx="41" cy="27" r="4" fill="#2d3557"/>
      </svg>
      <h3>Donate</h3>
      <p>Sed ut perspiciatis unde omnis iste natus error sit voluptatem accusantium doloremque laud antium, totam rem aperia m eaque ipsa quae.</p>
      <a href="#" class="btn">Give</a>
    </div>
    <div class="feature">
      <svg viewBox="0 0 80 80" fill="none" stroke="#2d3557" stroke-width="5">
        <circle cx="16" cy="22" r="7"/><circle cx="64" cy="22" r="7"/>
        <path d="M4 50c0-10 6-16 14-16M76 50c0-10-6-16-14-16"/>
        <circle cx="40" cy="20" r="11"/>
        <path d="M20 72c0-16 9-26 20-26s20 10 20 26z"/>
        <path d="M40 52v14M36 55h6a2.5 2.5 0 010 5h-4a2.5 2.5 0 000 5h6" stroke-width="2.5"/>
      </svg>
      <h3>Sponsor</h3>
      <p>Sed ut perspiciatis unde omnis iste natus error sit voluptatem accusantium doloremque laud antium, totam rem aperia m eaque ipsa quae.</p>
      <a href="#" class="btn">Sponsor an Animal</a>
    </div>
    <div class="feature">
      <svg viewBox="0 0 80 80">
        <path d="M40 44 C22 32 24 12 34 12 C38 12 40 16 40 18 C40 16 42 12 46 12 C56 12 58 32 40 44Z" fill="#2d3557"/>
        <path d="M6 30 L14 56 L30 70 M74 30 L66 56 L50 70 M14 40 L26 54 M66 40 L54 54" fill="none" stroke="#2d3557" stroke-width="5" stroke-linecap="round" stroke-linejoin="round"/>
      </svg>
      <h3>Tour</h3>
      <p>Sed ut perspiciatis unde omnis iste natus error sit voluptatem accusantium doloremque laud antium, totam rem aperia m eaque ipsa quae.</p>
      <a href="#" class="btn">Read More</a>
    </div>
  </div>
</section>

<section class="welcome">
  <div class="welcome-photo" role="img" aria-label="Sheep grazing in a sunlit meadow behind a dark wooden fence, with tall trees"></div>
  <div class="welcome-copy">
    <div class="lead">Welcome to</div>
    <h2>Cedar Hollow Farm.</h2>
    <span class="rule"></span>
    <p>At vero eos et accusamus et iusto odio dignissimos ducimus qui blanditiis praesentium voluptatum deleniti atque corrupti quos dolores et quas molestias excepturi sint occaecati cupiditate non provident, similique sunt in culpa qui officia deserunt mollitia animi, id est laborum et dolorum fuga. Et harum quidem rerum facilis est et expedita distinctio. Nam libero tempore, cum soluta nobis est eligendi optio placeat facere possimus, omnis voluptas assumenda est omnis dolor.</p>
    <a href="#" class="btn">Read More</a>
  </div>
</section>

<section class="services">
  <div class="services-photo" role="img" aria-label="A black and white cow standing in a green field under a deep blue sky, with a herd behind"></div>
  <svg class="edge" style="top:-1px;height:52px" viewBox="0 0 1200 52" preserveAspectRatio="none">
    <path fill="#ffffff" d="M0 0 L1200 0 L1200 6 L1160 18 L1110 10 L1060 24 L1010 16 L960 30 L910 22 L860 34 L810 28 L760 38 L700 32 L640 42 L580 36 L520 44 L460 38 L400 46 L340 40 L280 48 L220 42 L160 50 L100 44 L40 50 L0 46 Z"/>
  </svg>
  <div class="services-copy">
    <span class="bar"></span>
    <h2>Our Services</h2>
    <p class="intro">At vero eos et accusamus et iusto odio dignissimos ducimus qui blanditiis praesentium.</p>
    <ul>
      <li>Quas molestias excepturi sint</li>
      <li>At vero eos et accusamus et iusto</li>
      <li>On the other hand</li>
      <li>Nam libero temporecum soluta</li>
      <li>In a free hour when our power</li>
    </ul>
    <a href="#" class="btn">Read More</a>
  </div>
  <svg class="edge" style="bottom:-1px;height:44px" viewBox="0 0 1200 44" preserveAspectRatio="none">
    <path fill="#f4f2f2" d="M0 8 L50 20 L100 14 L150 26 L210 20 L260 30 L320 24 L380 32 L440 26 L500 34 L560 28 L620 36 L680 28 L740 34 L800 26 L860 32 L920 22 L980 28 L1040 18 L1100 24 L1160 12 L1200 18 L1200 44 L0 44 Z"/>
  </svg>
</section>

<section class="involved">
  <h2 class="section-title">Get Involved</h2>
  <span class="rule"></span>
  <svg class="arrow prev" viewBox="0 0 20 30"><path d="M15 3 L5 15 L15 27" fill="none" stroke="#b0b0b0" stroke-width="2"/></svg>
  <div class="cards">
    <article class="card">
      <div class="card-photo cow" role="img" aria-label="A brown cow with horns standing in tall grass"></div>
      <div class="card-body">
        <h3>Lorem Ipsum is simply</h3>
        <p>At vero eos et accusamus et iusto odio dignissimos ducimus qui blanditiis praesentium.</p>
        <a href="#" class="btn">Read More</a>
      </div>
    </article>
    <article class="card">
      <div class="card-photo goat" role="img" aria-label="A white goat among green leaves"></div>
      <div class="card-body">
        <h3>Lorem Ipsum is simply</h3>
        <p>At vero eos et accusamus et iusto odio dignissimos ducimus qui blanditiis praesentium.</p>
        <a href="#" class="btn">Read More</a>
      </div>
    </article>
    <article class="card">
      <div class="card-photo horses" role="img" aria-label="Two brown horses walking across an autumn field"></div>
      <div class="card-body">
        <h3>Lorem Ipsum is simply</h3>
        <p>At vero eos et accusamus et iusto odio dignissimos ducimus qui blanditiis praesentium.</p>
        <a href="#" class="btn">Read More</a>
      </div>
    </article>
  </div>
  <svg class="arrow next" viewBox="0 0 20 30"><path d="M5 3 L15 15 L5 27" fill="none" stroke="#b0b0b0" stroke-width="2"/></svg>
</section>

<section class="donation">
  <h2 class="section-title">Make a Donation</h2>
  <p>At vero eos et accusamus et iusto odio dignissimos ducimus qui blanditiis praesentium voluptatum deleniti atque.</p>
  <a href="#" class="btn">Donate Today</a>
</section>

<footer class="site-footer">
  <svg class="edge" style="top:-1px;height:40px" viewBox="0 0 1200 40" preserveAspectRatio="none">
    <path fill="#ffffff" d="M0 0 L1200 0 L1200 22 L1150 14 L1100 26 L1040 16 L980 28 L920 18 L860 30 L800 20 L740 30 L680 18 L620 28 L560 16 L500 26 L440 14 L380 24 L320 12 L260 22 L200 10 L140 20 L80 8 L30 16 L0 6 Z"/>
  </svg>
  <div class="footer-brand">Cedar Hollow Farm</div>
  <div class="footer-col contact">
    <h4>Contact Us</h4>
    <div class="contact-item">
      <svg viewBox="0 0 12 12"><path d="M6 0a4 4 0 014 4c0 3-4 8-4 8S2 7 2 4a4 4 0 014-4z" fill="#fff"/><circle cx="6" cy="4" r="1.5" fill="#2d3557"/></svg>
      <span>Meadowbrook Lane 24<br>4821 KL Harlow Vale</span>
    </div>
    <div class="contact-item">
      <svg viewBox="0 0 12 12"><path d="M2 1l2.5-.5 1.5 3-1.5 1a6 6 0 003 3l1-1.5 3 1.5-.5 2.5C6 11 1 6 2 1z" fill="#fff"/></svg>
      <span>555.010.2468</span>
    </div>
    <div class="contact-item">
      <svg viewBox="0 0 12 12"><rect x="0.5" y="2" width="11" height="8" fill="#fff"/><path d="M0.5 2l5.5 4.5L11.5 2" fill="none" stroke="#2d3557" stroke-width="1"/></svg>
      <span>hello@cedarhollowfarm.org</span>
    </div>
  </div>
  <div class="footer-col menu">
    <h4>Menu</h4>
    <ul>
      <li>Home</li><li>About</li><li>Meet The Animals</li><li>Get Involved</li><li>Contact Us</li><li>Donate</li>
    </ul>
  </div>
  <div class="footer-col connect">
    <h4>Connect With Us</h4>
    <div class="social"><span class="dot a"></span>Newsfeed</div>
    <div class="social"><span class="dot b"></span>Updates</div>
    <div class="social"><span class="dot c"></span>Network</div>
  </div>
  <div class="copyright">Copyrights @ 2019 All Rights Reserved</div>
</footer>

</body>
</html>
```